Business / Discount Card

Looking to create a 2 sided business card. Front side to say "Thanks for flying with Skyward Drifting" then have link to "In-Flight Photos, www.skywarddrifting.com.au, password: skyward" Back side of card to have company logo, phone number, facebook & instagram logo and #skywarddrifting. Also included on this side will be discount text "Book again and save 10%. Use discount code: skyward10"Round Corner Card Templates are attached. Please ensure dimensions are correct.Thanks,

Font styles to use
Sans Serif

Colors
33a6d7
ffffff
000000

Requirements
Must have
• Logo
• Blue, White and Black color scheme

```html
<!DOCTYPE html>
<html lang="en">
<head>
<meta charset="utf-8">
<title>Skyward Drifting – Thank You Card</title>
<link rel="stylesheet" href="https://fonts.googleapis.com/css2?family=Oswald:wght@600&family=Roboto:ital,wght@0,400;0,500;0,700;1,400;1,700&family=Pacifico&display=swap">
<style>
  :root {
    --sky-blue: #33a6d7;
    --ink: #000000;
    --paper: #ffffff;
    --backdrop: #f2f3f4;
    --paper-tint: #f5f5f5;
  }
  * { box-sizing: border-box; margin: 0; padding: 0; }
  html, body { width: 1200px; height: 1000px; overflow: hidden; }
  body {
    background: var(--backdrop);
    position: relative;
    font-family: "Roboto", Arial, sans-serif;
  }
  .card {
    position: absolute;
    left: 300px;
    width: 598px;
    height: 377px;
    border-radius: 22px;
    overflow: hidden;
  }
  .card--front { top: 95px; background: var(--paper-tint); }
  .card--back { top: 518px; background: var(--ink); }

  .front-bands { position: absolute; inset: 0; }

  .brand-dot {
    position: absolute;
    top: 22px;
    width: 80px;
    height: 80px;
    border-radius: 50%;
    background: var(--sky-blue);
  }
  .brand-dot--left { left: 30px; }
  .brand-dot--right { right: 30px; }

  .thanks {
    position: absolute;
    top: 98px;
    left: 0;
    width: 100%;
    text-align: center;
    color: var(--ink);
  }
  .thanks__line {
    font-family: "Oswald", Arial, sans-serif;
    font-weight: 600;
    font-size: 37px;
    line-height: 48px;
    display: block;
  }
  .thanks__joiner {
    font-family: "Pacifico", cursive;
    color: var(--sky-blue);
    font-size: 26px;
    line-height: 36px;
    display: block;
  }

  .photos {
    position: absolute;
    left: 0;
    width: 100%;
    top: 314px;
    text-align: center;
    color: var(--ink);
  }
  .photos__title {
    font-family: "Oswald", Arial, sans-serif;
    font-weight: 600;
    font-size: 20px;
    line-height: 24px;
  }
  .photos__link {
    font-family: "Roboto", Arial, sans-serif;
    font-weight: 500;
    font-size: 18px;
    line-height: 22px;
  }

  .wordmark {
    position: absolute;
    top: 62px;
    left: 0;
    width: 100%;
    display: flex;
    justify-content: center;
    align-items: center;
    gap: 16px;
  }
  .wordmark__dot {
    width: 56px;
    height: 56px;
    border-radius: 50%;
    background: var(--sky-blue);
  }
  .wordmark__name {
    font-family: "Roboto", Arial, sans-serif;
    font-weight: 700;
    font-size: 50px;
    color: var(--sky-blue);
    line-height: 1;
  }
  .offer {
    position: absolute;
    left: 112px;
    top: 204px;
    width: 371px;
    height: 58px;
    border-radius: 29px;
    background: var(--sky-blue);
    color: var(--paper);
    text-align: center;
    font-style: italic;
    font-size: 19px;
    line-height: 23px;
    padding-top: 6px;
  }
  .offer strong { font-weight: 700; }
  .phone {
    position: absolute;
    top: 285px;
    width: 100%;
    text-align: center;
    color: var(--sky-blue);
    font-weight: 700;
    font-size: 23px;
  }
  .social {
    position: absolute;
    top: 310px;
    width: 100%;
    display: flex;
    justify-content: center;
    align-items: center;
    gap: 10px;
  }
  .social__dot {
    width: 36px;
    height: 36px;
    border-radius: 50%;
    background: var(--sky-blue);
  }
  .social__tag {
    color: var(--paper);
    font-weight: 500;
    font-size: 23px;
  }
</style>
</head>
<body>

<section class="card card--front" aria-label="Card front">
  <svg class="front-bands" width="598" height="377" viewBox="0 0 598 377" aria-hidden="true">
    <path d="M0 228 Q299 300 598 228 L598 377 L0 377 Z" fill="var(--ink)"/>
    <path d="M0 318 Q299 262 598 318 L598 377 L0 377 Z" fill="var(--paper)"/>
    <path d="M0 326 Q299 270 598 326 L598 377 L0 377 Z" fill="var(--sky-blue)"/>
  </svg>
  <span class="brand-dot brand-dot--left" aria-hidden="true"></span>
  <span class="brand-dot brand-dot--right" aria-hidden="true"></span>
  <h1 class="thanks">
    <span class="thanks__line">THANKS FOR FLYING</span>
    <span class="thanks__joiner">with</span>
    <span class="thanks__line">SKYWARD DRIFTING</span>
  </h1>
  <div class="photos">
    <p class="photos__title">IN-FLIGHT PHOTOS</p>
    <p class="photos__link">www.skywarddrifting.com.au, Password: skyward</p>
  </div>
</section>

<section class="card card--back" aria-label="Card back">
  <div class="wordmark">
    <span class="wordmark__dot" aria-hidden="true"></span>
    <span class="wordmark__name">Skyward Drifting</span>
  </div>
  <p class="offer">Book again and save <strong>10%</strong><br>Use discount code: <strong>skyward10</strong></p>
  <p class="phone">1300 555 019</p>
  <div class="social">
    <span class="social__dot" aria-hidden="true"></span>
    <span class="social__tag">#skywarddrifting</span>
    <span class="social__dot" aria-hidden="true"></span>
  </div>
</section>

</body>
</html>
```